Small Cosmetics Business needs a label design

We need a label design to affix on our cosmetic products made in Norfolk, England. The label needs to have the manufacturer's name, the product name, an ingredients list, an indication of use (ritual), contact details of manufacturer, weight, period after opening logo, batch number. We would like the label to highlight (in the form of sticker or tags) that the products are 100% natural, that they are hand made, that they do not contain preservatives or chemicals.Attached is a file with typical information for the label. The label should have colours, clarity and evoke nature, luxury.

Target Market(s)

UK

Industry/Entity Type

Cosmetics

Logo Text

Toril Sefa, Shape Grace

Font styles to use
Decorative

```html
<!DOCTYPE html>
<html lang="en">
<head>
<meta charset="utf-8">
<title>Toril Sefa – Coco Haven Label</title>
<link rel="stylesheet" href="https://fonts.googleapis.com/css2?family=Great+Vibes&family=Josefin+Sans:wght@400&family=Pathway+Gothic+One&family=Questrial&display=swap">
<style>
  :root {
    --backdrop-light: #ffffff;
    --backdrop-dark: #e4e4e4;
    --label-white: #ffffff;
    --label-edge: #8a8a8a;
    --accent-peach: #f0a476;
    --ink: #262626;
    --ink-brown: #4a3a33;
    --ink-grey: #4d4d4d;
    --flora-green: #d6e7dc;
    --flora-grey: #eeeeee;
  }
  * { margin: 0; padding: 0; box-sizing: border-box; }
  html, body { width: 1200px; height: 438px; overflow: hidden; }
  body {
    background: radial-gradient(ellipse at 50% 40%, var(--backdrop-light) 0%, var(--backdrop-dark) 100%);
    position: relative;
  }
  .label {
    position: absolute;
    left: 80px; top: 137px;
    width: 1060px; height: 147px;
    background: var(--label-white);
    border: 1px solid var(--label-edge);
    overflow: hidden;
  }
  .flora-strip {
    position: absolute; left: 0; width: 100%;
    background: linear-gradient(90deg,
      var(--flora-grey) 0%, var(--flora-green) 12%, var(--flora-grey) 24%,
      var(--flora-green) 40%, var(--flora-grey) 52%, var(--flora-green) 66%,
      var(--flora-grey) 78%, var(--flora-green) 90%, var(--flora-grey) 100%);
  }
  .flora-strip--top { top: 0; height: 40px; }
  .flora-strip--bottom { bottom: 0; height: 11px; }

  .ritual {
    position: absolute; left: 14px; top: 55px; width: 142px;
    font-family: "Pathway Gothic One", sans-serif;
    font-size: 9.8px; line-height: 12.4px; color: var(--ink);
  }
  .ritual__title { color: var(--accent-peach); }

  .maker-details {
    position: absolute; left: 170px; top: 57px; width: 210px;
    font-family: "Pathway Gothic One", sans-serif;
    font-size: 7.8px; line-height: 10px; color: var(--ink);
  }

  .brand__name,
  .brand__product,
  .brand__claims {
    position: absolute; left: 314px; width: 440px;
    text-align: center; white-space: nowrap;
  }
  .brand__name {
    top: 44px;
    font-family: "Great Vibes", cursive;
    font-size: 40px; line-height: 44px;
    color: var(--accent-peach);
  }
  .brand__product {
    top: 94px;
    font-family: "Josefin Sans", sans-serif;
    font-size: 12.5px; line-height: 14px; letter-spacing: 5px;
    color: var(--ink-brown);
  }
  .brand__claims {
    top: 115px;
    font-family: "Questrial", sans-serif;
    font-size: 9.4px; line-height: 12px; color: var(--ink-grey);
  }

  .ingredients {
    position: absolute; left: 725px; top: 59px; width: 327px;
    font-family: "Pathway Gothic One", sans-serif;
    font-style: italic;
    font-size: 8px; line-height: 10.4px; color: var(--ink);
  }
  .ingredients__title { color: var(--accent-peach); }
</style>
</head>
<body>
  <section class="label">
    <div class="flora-strip flora-strip--top" role="img" aria-label="Hand-drawn tropical flowers and leaves pattern in grey line art with soft green washes"></div>

    <div class="ritual">
      <p class="ritual__title">Ritual:</p>
      <p>Use for wet or dry hair. Apply to the length of the hair focussing on the ends. Leave 15 minutes then rinse with either water or a light shampoo and style as wished.</p>
    </div>

    <div class="maker-details">
      <p>For period after opening use icon similar to the following:</p>
      <p>Manufactured by Toril Sefa Ltd,</p>
      <p>P.O. Box 418 Lowmere LM12 4QX, UK</p>
      <p>Batch number:</p>
      <p>Weight:</p>
    </div>

    <p class="brand__name">Toril Sefa</p>
    <p class="brand__product">COCO HAVEN</p>
    <p class="brand__claims">100% Natural | Handmade in Norfolk &nbsp;| Contains No Preservatives and No Chemicals</p>

    <p class="ingredients"><span class="ingredients__title">Ingredients:</span> Cocos Nucifera Coconut) Oil , Elaeis Guineensis (Sustainable Palm) Oil, Olea Europaea (Olive) Fruit Oil, Helianthus Annus (Sunflower) Seed Oil, &nbsp;Butyrospermum Parkii (Shea Butter), Oryza Sativa (Rice Bran) Oil, Argania Spinosa Kernel (Argan) Oil, Persea Gratissima (Avocado) Oil, Simmondsia Chinensis (Jojoba) Seed Oil, Ricinus Communis (Castor) Seed Oil, Cera Alba (Beeswax), Canaga Odorata (Ylang Ylang) Flower Oil, Citrus Aurantium Dulcis (Orange) Peel Oil.</p>

    <div class="flora-strip flora-strip--bottom" role="img" aria-label="Continuation of the hand-drawn tropical flower and leaf pattern"></div>
  </section>
</body>
</html>
```